Bramfield Animal Hospital brochure

We have found that our current clients do not know all of the services that we offer so we want to make a hospital brochure to make our services more known. Our website has all of our services listed but we find that clients aren't looking at our website as much as we would like so we are hoping a hospital brochure can sum up our main services and maybe lead to more people visiting our website. Our hospital colors are blue and maroon and our moto is "Outstanding Medicine, Extraordinary Service." Some of the service we would like to promote more include digital x-ray, ultrasounds, echocardiograms, laser therapy and dentals. We also offer after hours emergency care but only to our current clients. You can find more services listed on our website We are in a small town so we want a personal yet professional feel.

Feel free to visit our website to get a better feel for our business https://thecorvelpets.com/

• 6-8 panel brochure
• I included some photos from around the hospital. If you feel that you can make a few work in the brochure then great but don't feel obligated to.

```html
<!DOCTYPE html>
<html lang="en">
<head>
<meta charset="utf-8">
<title>Bramfield Animal Hospital – Brochure</title>
<link rel="stylesheet" href="https://fonts.googleapis.com/css2?family=Domine:wght@700&family=Tinos:wght@400;700&display=swap">
<style>
  :root{
    --maroon:#8c1a0b;
    --maroon-dark:#6a1107;
    --gold:#f2c27c;
    --cream:#fde3ad;
    --cream-deep:#fbd193;
    --pink:#ea5b70;
    --ink:#2b1a16;
    --white:#ffffff;
    --page:#d7d7d7;
    --dot:rgba(240,190,170,.75);
  }
  *{box-sizing:border-box;margin:0;padding:0}
  html,body{width:1200px;height:2897px;overflow:hidden}
  body{background:var(--page);font-family:"Tinos",serif;color:var(--white);position:relative}
  .spread{position:absolute;left:60px;width:1080px;height:766px;overflow:hidden;box-shadow:0 22px 30px -14px rgba(0,0,0,.35)}
  .spread--outside{top:622px}
  .spread--inside{top:1508px}
  .panel{position:absolute;top:0;height:100%;overflow:hidden}
  .maroon{background:linear-gradient(160deg,var(--maroon) 40%,var(--maroon-dark))}
  .photo{position:absolute}
  .circle{border-radius:50%}
  .ring{position:absolute;border:1.5px solid rgba(255,255,255,.8);border-radius:50%}
  .dot{position:absolute;border-radius:50%;background:var(--dot)}
  .heading{font-family:"Domine",serif;font-weight:700;color:var(--gold)}
  .quote{position:absolute;color:var(--white)}
  .quote-mark{position:absolute;font-family:"Domine",serif;font-size:28px;color:var(--white);line-height:1}

  /* outside spread */
  .panel--story{left:0;width:380px}
  .panel--story .heading{position:absolute;left:64px;top:78px;font-size:20px}
  .panel--story .quote{left:64px;top:116px;width:290px;font-size:13.5px;line-height:16.5px}
  .panel--info{left:380px;width:340px}
  .pin{position:absolute;left:150px;top:222px;width:40px;height:36px}
  .address{position:absolute;left:18px;top:273px;width:308px;height:112px;border:1.5px solid rgba(255,255,255,.85);padding:18px 20px;font-size:19px;line-height:1.5;font-style:normal}
  .panel--info .heading.hours-title{position:absolute;left:46px;top:420px;font-family:"Tinos",serif;font-weight:400;font-size:27px}
  .hours{position:absolute;left:46px;top:468px;font-size:15.5px;line-height:21.5px}
  .contact{position:absolute;left:46px;top:672px;font-size:14px;line-height:19px;list-style:none}
  .contact li{display:flex;align-items:center;gap:8px}
  .contact svg{width:12px;height:12px;fill:var(--white)}
  .panel--cover{left:720px;width:360px;background:var(--white)}
  .brand{position:absolute;left:0;top:470px;width:100%;display:flex;align-items:center;justify-content:center;gap:10px;font-family:"Tinos",serif;font-size:22px;color:var(--maroon);text-align:center;line-height:1.1}
  .brand-mark{width:16px;height:16px;border-radius:50%;background:var(--maroon);flex:none}
  .tagline{position:absolute;left:58px;top:612px;padding-left:14px;border-left:2px solid var(--maroon);color:var(--maroon)}
  .tagline .line1{font-family:"Domine",serif;font-weight:700;font-size:27px;line-height:1.2;display:block}
  .tagline .line2{font-family:"Tinos",serif;font-weight:700;font-size:18px;color:var(--ink);display:block;margin-top:4px}

  /* inside spread */
  .panel--services{left:0;width:361px;background:linear-gradient(180deg,var(--cream-deep),var(--cream))}
  .panel--services .heading{position:absolute;top:24px;width:100%;text-align:center;font-size:24px;color:var(--maroon)}
  .service{position:absolute;width:150px;text-align:center;font-size:12px;line-height:1.2;color:var(--maroon)}
  .service .photo{position:relative;display:block;width:90px;height:90px;margin:0 auto 6px;border:2px solid rgba(255,255,255,.6)}
  .panel--more{left:361px;width:346px}
  .more-box{position:absolute;left:26px;top:287px;width:309px;height:462px;border:1.5px solid rgba(255,255,255,.85)}
  .more-box .heading{position:absolute;top:-13px;left:20px;padding:0 8px;font-family:"Tinos",serif;font-weight:400;font-size:18px;background:var(--maroon)}
  .more-list{position:absolute;left:22px;top:24px;list-style:none;font-size:12.5px;font-weight:700;line-height:30.5px}
  .more-list li{display:flex;align-items:center;gap:10px}
  .more-list svg{width:11px;height:11px}
  .panel--welcome{left:707px;width:373px}
  .panel--welcome .quote{left:71px;top:63px;width:232px;font-size:11.5px;line-height:16px;font-weight:700}
</style>
</head>
<body>

<section class="spread spread--outside" aria-label="Brochure outside">
  <div class="panel panel--story maroon">
    <h2 class="heading">Compassion and Empathy</h2>
    <span class="quote-mark" style="left:36px;top:116px">“</span>
    <p class="quote">We believe in building something special. Taking care of you and your pet like family is the only way we know how to live. In order to do that, we take the time to listen. To connect. To understand. And to teach. We believe that veterinary care is at its best when it involves you, and your deeper concerns or goals for your pet are addressed. There is an uncommon warmth here, a special kind of culture. We do it because the love you share with your pet is precious. And to us, you are a hero for caring the way you do for your companion.</p>
    <span class="quote-mark" style="left:286px;top:338px">”</span>
    <div class="ring" style="left:-25px;top:398px;width:390px;height:390px"></div>
    <div class="photo circle" role="img" aria-label="Portrait of a boxer dog on a cream background" style="left:-12px;top:411px;width:364px;height:364px;background:radial-gradient(circle at 55% 45%,#c98a4c,#8a5a30 40%,#f3e7d3 72%)"></div>
    <div class="dot" style="left:44px;top:383px;width:36px;height:36px"></div>
    <div class="dot" style="left:178px;top:373px;width:20px;height:20px"></div>
  </div>

  <div class="panel panel--info maroon">
    <div class="ring" style="left:-10px;top:-90px;width:354px;height:354px"></div>
    <div class="photo circle" role="img" aria-label="Person relaxing on a sofa with a small dog" style="left:0;top:-80px;width:334px;height:334px;background:radial-gradient(circle at 50% 60%,#d9d4cf,#8f97a3 55%,#4a5a70)"></div>
    <div class="dot" style="left:45px;top:150px;width:40px;height:40px"></div>
    <svg class="pin" viewBox="0 0 40 36" aria-hidden="true">
      <path d="M20 3a8 8 0 0 0-8 8c0 6 8 14 8 14s8-8 8-14a8 8 0 0 0-8-8zm0 11a3 3 0 1 1 0-6 3 3 0 0 1 0 6z" fill="none" stroke="#f2c27c" stroke-width="2"/>
      <path d="M2 30h14M24 30h14" stroke="#f2c27c" stroke-width="1.5"/>
    </svg>
    <address class="address">Bramfield Animal Hospital<br>418 Orchard Road<br>Bramfield, Vermont, 05199</address>
    <h3 class="heading hours-title">Hospital Hours</h3>
    <p class="hours">Monday 8:00am - 5:00pm<br>Tuesday 8:0am - 8:00pm<br>Wednesday 8:00am- 5:00pm<br>Thursday 8:00am - 6:00pm<br>Friday 8:00am - 4:00pm<br>Saturday 8:00am - 1:00pm<br>Sunday Closed</p>
    <ul class="contact">
      <li><svg viewBox="0 0 12 12"><path d="M2.5 1l2 2-1 1.5a7 7 0 0 0 4 4L9 7.5l2 2-1.5 1.5C5 11 1 7 1 2.5z"/></svg>802-555-0148</li>
      <li><svg viewBox="0 0 12 12"><path d="M3 1h6v3H3zM1 5h10v4H9v2H3V9H1zM4 8h4v2H4z"/></svg>802-555-0172</li>
      <li><svg viewBox="0 0 12 12"><path d="M1 2h10v8H1zM1.5 2.5 6 6.5l4.5-4" stroke="#8c1a0b" stroke-width="1"/></svg>info@thecorvelpets.com</li>
    </ul>
  </div>

  <div class="panel panel--cover">
    <div class="photo" role="img" aria-label="Smiling woman holding two puppies against a pink wall" style="left:0;top:0;width:360px;height:430px;background:linear-gradient(180deg,var(--pink) 0%,#e98a85 45%,#d9a57b 65%,#ffffff 100%)"></div>
    <div class="brand"><span class="brand-mark"></span><span>Bramfield<br>Animal Hospital</span></div>
    <p class="tagline"><span class="line1">Outstanding<br>Medicine,</span><span class="line2">Extraordinary Service</span></p>
  </div>
</section>

<section class="spread spread--inside" aria-label="Brochure inside">
  <div class="panel panel--services">
    <h2 class="heading">Our Services</h2>
    <div class="service" style="left:45px;top:58px"><span class="photo circle" role="img" aria-label="Dog and cat together outdoors" style="background:radial-gradient(circle,#cfd2c5,#6f8a4e)"></span>Allergy and<br>Dermatology Testing</div>
    <div class="service" style="left:198px;top:58px"><span class="photo circle" role="img" aria-label="Dark cat on a grey background" style="background:radial-gradient(circle,#5a5048,#2a2522 60%,#8fa39a)"></span>Flea and Tick<br>Prevention</div>
    <div class="service" style="left:45px;top:204px"><span class="photo circle" role="img" aria-label="Dog running on grass" style="background:radial-gradient(circle,#3a2a20,#4d7a35 60%)"></span>Cardiology Care</div>
    <div class="service" style="left:198px;top:204px"><span class="photo circle" role="img" aria-label="Red laser light on black" style="background:radial-gradient(circle,#e23a2a,#5a0d08 35%,#0d0505)"></span>Cold Laser Therapy</div>
    <div class="service" style="left:45px;top:339px"><span class="photo circle" role="img" aria-label="Cat silhouette at sunset" style="background:radial-gradient(circle at 50% 70%,#3a1c10,#e9875a 50%,#f6c59b)"></span>End-Of-Life Care</div>
    <div class="service" style="left:198px;top:339px"><span class="photo circle" role="img" aria-label="Ferret curled up" style="background:radial-gradient(circle,#e6dbc8,#6a5a48 70%)"></span>Exotic Pet Care</div>
    <div class="service" style="left:45px;top:483px"><span class="photo circle" role="img" aria-label="Pet food bowl" style="background:radial-gradient(circle,#7a3a18,#3a1a0e 70%)"></span>Nutritional<br>Consultations</div>
    <div class="service" style="left:198px;top:483px"><span class="photo circle" role="img" aria-label="Rottweiler resting outdoors" style="background:radial-gradient(circle,#2a2220,#4c6a3c 65%)"></span>Orthopedic<br>Surgery</div>
    <div class="service" style="left:45px;top:628px"><span class="photo circle" role="img" aria-label="Happy senior dog" style="background:radial-gradient(circle,#e8e0d8,#2a2624 60%,#cfd8dc)"></span>Senior Wellness</div>
    <div class="service" style="left:198px;top:628px"><span class="photo circle" role="img" aria-label="Cat resting after surgery" style="background:radial-gradient(circle,#d9a874,#6e5a4a 65%)"></span>Soft Tissue Surgery</div>
  </div>

  <div class="panel panel--more maroon">
    <div class="ring" style="left:14px;top:-76px;width:320px;height:320px"></div>
    <div class="photo circle" role="img" aria-label="Golden retriever cuddling a grey cat" style="left:24px;top:-66px;width:300px;height:300px;background:radial-gradient(circle at 55% 45%,#c98a45,#a06a3c 40%,#7e7f86 65%,#e9e6e0)"></div>
    <div class="dot" style="left:55px;top:206px;width:36px;height:36px"></div>
    <div class="more-box">
      <h3 class="heading">Some of other service</h3>
      <ul class="more-list">
        <li><svg viewBox="0 0 11 11"><rect x=".5" y=".5" width="10" height="10" fill="none" stroke="#fff"/><path d="M2.5 5.5l2 2 4-4.5" fill="none" stroke="#fff" stroke-width="1.4"/></svg>Blood Tests and Urine Screening</li>
        <li><svg viewBox="0 0 11 11"><rect x=".5" y=".5" width="10" height="10" fill="none" stroke="#fff"/><path d="M2.5 5.5l2 2 4-4.5" fill="none" stroke="#fff" stroke-width="1.4"/></svg>Canine and Feline Dental Care</li>
        <li><svg viewBox="0 0 11 11"><rect x=".5" y=".5" width="10" height="10" fill="none" stroke="#fff"/><path d="M2.5 5.5l2 2 4-4.5" fill="none" stroke="#fff" stroke-width="1.4"/></svg>Digital X-Ray</li>
        <li><svg viewBox="0 0 11 11"><rect x=".5" y=".5" width="10" height="10" fill="none" stroke="#fff"/><path d="M2.5 5.5l2 2 4-4.5" fill="none" stroke="#fff" stroke-width="1.4"/></svg>Emergency Care</li>
        <li><svg viewBox="0 0 11 11"><rect x=".5" y=".5" width="10" height="10" fill="none" stroke="#fff"/><path d="M2.5 5.5l2 2 4-4.5" fill="none" stroke="#fff" stroke-width="1.4"/></svg>Eye Care</li>
        <li><svg viewBox="0 0 11 11"><rect x=".5" y=".5" width="10" height="10" fill="none" stroke="#fff"/><path d="M2.5 5.5l2 2 4-4.5" fill="none" stroke="#fff" stroke-width="1.4"/></svg>House Calls</li>
        <li><svg viewBox="0 0 11 11"><rect x=".5" y=".5" width="10" height="10" fill="none" stroke="#fff"/><path d="M2.5 5.5l2 2 4-4.5" fill="none" stroke="#fff" stroke-width="1.4"/></svg>Parasite Testing and Treatment</li>
        <li><svg viewBox="0 0 11 11"><rect x=".5" y=".5" width="10" height="10" fill="none" stroke="#fff"/><path d="M2.5 5.5l2 2 4-4.5" fill="none" stroke="#fff" stroke-width="1.4"/></svg>Puppy and Kitten Care</li>
        <li><svg viewBox="0 0 11 11"><rect x=".5" y=".5" width="10" height="10" fill="none" stroke="#fff"/><path d="M2.5 5.5l2 2 4-4.5" fill="none" stroke="#fff" stroke-width="1.4"/></svg>Ultrasound</li>
        <li><svg viewBox="0 0 11 11"><rect x=".5" y=".5" width="10" height="10" fill="none" stroke="#fff"/><path d="M2.5 5.5l2 2 4-4.5" fill="none" stroke="#fff" stroke-width="1.4"/></svg>Vaccinations</li>
        <li><svg viewBox="0 0 11 11"><rect x=".5" y=".5" width="10" height="10" fill="none" stroke="#fff"/><path d="M2.5 5.5l2 2 4-4.5" fill="none" stroke="#fff" stroke-width="1.4"/></svg>Echocardiograms</li>
        <li><svg viewBox="0 0 11 11"><rect x=".5" y=".5" width="10" height="10" fill="none" stroke="#fff"/><path d="M2.5 5.5l2 2 4-4.5" fill="none" stroke="#fff" stroke-width="1.4"/></svg>Dentals</li>
        <li><svg viewBox="0 0 11 11"><rect x=".5" y=".5" width="10" height="10" fill="none" stroke="#fff"/><path d="M2.5 5.5l2 2 4-4.5" fill="none" stroke="#fff" stroke-width="1.4"/></svg>Digital x-ray</li>
        <li><svg viewBox="0 0 11 11"><rect x=".5" y=".5" width="10" height="10" fill="none" stroke="#fff"/><path d="M2.5 5.5l2 2 4-4.5" fill="none" stroke="#fff" stroke-width="1.4"/></svg>Laser therapy</li>
      </ul>
    </div>
  </div>

  <div class="panel panel--welcome maroon">
    <span class="quote-mark" style="left:42px;top:60px">“</span>
    <p class="quote">We built Bramfield Animal Hospital for you. It is so important to us that you can walk into an environment where you feel you are always put first, and where the little things have been thought of to make this a truly wonderful experience. We want to make your life easier. We offer evening hours, drop-offs, and house call appointments. And existing clients get access to 24 hour emergency care. Because we are always looking out for you.</p>
    <span class="quote-mark" style="left:256px;top:286px">”</span>
    <div class="photo" role="img" aria-label="Tan and white dog raising one paw" style="left:30px;top:533px;width:303px;height:233px;background:radial-gradient(ellipse at 50% 60%,#f1e6da 0%,#c7844c 40%,rgba(140,26,11,0) 72%)"></div>
  </div>
</section>

</body>
</html>
```